Paint Protection Options

This is a flyer that will describe two different paint protection options for vehicles. I have mocked up a Word doc. As well, I've included some samples of other flyers where I like the "look". I am not locked into any single layout or design. In my Word doc I have them side-by-side. I think that makes sense but open to ideas. I've also added some pics of the two options being applied to cars. We need to have one of each (ceramic and ppf) at a minimum. In the grid I'm thinking different colors dots/circles to differentiate the different levels. But again, I'm open to suggestions. You can use the symbol for microns in the grid under the Thickness row. I spelled it out because I didn't know how to insert.

```html
<!DOCTYPE html>
<html lang="en">
<head>
<meta charset="utf-8">
<title>Paint Protection Options</title>
<link href="https://fonts.googleapis.com/css2?family=Poppins:wght@500;600;700;800&family=Figtree:wght@400;500;600&display=swap" rel="stylesheet">
<style>
:root{
  --backdrop:#a5a5a5;
  --paper:#ffffff;
  --blue:#1f5fb5;
  --blue-light:#2ea3e0;
  --navy:#163f8c;
  --orange:#f28a1f;
  --green:#52a844;
  --ink:#2b2b2b;
  --feature-bg:#454545;
  --feature-head:#1f1f1f;
  --cell-bg:#f2f2f2;
  --rule:#9a9a9a;
  --tick-green:#3fae49;
  --tick-yellow:#d9c332;
  --tick-dark:#1d6b3a;
  --tick-red:#e0262b;
  --icon-blue:#1a83c6;
}
*{box-sizing:border-box;margin:0;padding:0}
html,body{width:1200px;height:1200px;overflow:hidden;background:var(--backdrop)}
.flyer{position:absolute;left:225px;top:70px;width:751px;height:1061px;background:var(--paper);font-family:"Figtree",sans-serif;color:var(--ink);overflow:hidden}
.masthead{position:absolute;left:0;top:0;width:751px;height:105px}
.masthead svg{position:absolute;inset:0}
.masthead-title{position:absolute;left:32px;top:23px;font-family:"Poppins",sans-serif;font-weight:800;font-size:33px;line-height:31px;color:#fff;letter-spacing:.3px}
.option-tab{position:absolute;left:40px;width:30px;background:var(--orange);display:flex;align-items:center;justify-content:center}
.option-tab span{transform:rotate(-90deg);white-space:nowrap;color:#fff;font-weight:600;font-size:19px}
.option-copy{position:absolute;left:83px;width:400px;font-size:10.6px;line-height:13.7px}
.option-copy p{margin-bottom:10.5px}
.benefits{list-style:none;margin-top:4px}
.benefits li{position:relative;padding-left:15px;font-size:11.8px;font-weight:500;line-height:15.2px;color:#1d1d1d}
.benefits li::before{content:"";position:absolute;left:2px;top:3.5px;border-left:7px solid var(--orange);border-top:4.5px solid transparent;border-bottom:4.5px solid transparent}
.option-photo{position:absolute;left:494px;width:219px;height:178px}
.divider{position:absolute;left:40px;top:333px;width:670px;border-top:1px dashed #777}

.compare{position:absolute;left:45px;top:578px;width:617px}
.compare-head{display:grid;grid-template-columns:209px 136px 136px 136px;height:57px;position:relative}
.head-feature{background:linear-gradient(135deg,#2a2a2a 60%,#3b3b3b 80%,#1a1a1a);border-top-left-radius:20px;color:#fff;font-family:"Poppins",sans-serif;font-weight:700;font-size:19px;padding:22px 0 0 27px}
.head-option{position:relative;border-top-left-radius:18px;border-top-right-radius:18px;color:#fff;font-family:"Poppins",sans-serif;font-weight:500;font-size:12.6px;text-align:center;padding-top:27px;margin-left:1px}
.head-option.wax{background:linear-gradient(160deg,#4a82d0,var(--blue))}
.head-option.ceramic{background:linear-gradient(160deg,#6cbd55,var(--green))}
.head-option.film{background:linear-gradient(160deg,#f5a847,var(--orange))}
.badge{position:absolute;left:50%;top:-10px;width:36px;height:36px;margin-left:-18px;border-radius:50%;border:2px solid #fff}
.wax .badge{background:var(--navy)}
.ceramic .badge{background:#4f9f3f}
.film .badge{background:#e07a1c}
.badge i{position:absolute;inset:7px;border:1.5px solid #fff;border-radius:5px}
.compare-row{display:grid;grid-template-columns:209px 136px 136px 136px;height:32.7px;border-bottom:1px solid var(--rule)}
.compare-row .feature{background:var(--feature-bg);color:#fff;font-weight:600;font-size:12.4px;display:flex;align-items:center;padding-left:18px;border-bottom:1px solid #5c5c5c;margin-bottom:-1px}
.feature-icon{width:27px;height:27px;border-radius:50%;background:var(--icon-blue);margin-right:7px;position:relative;flex:none}
.feature-icon::after{content:"";position:absolute;inset:8px;border:1.4px solid #fff;border-radius:50%}
.compare-row .cell{background:var(--cell-bg);display:flex;align-items:center;justify-content:center;font-size:11.6px;color:#222;border-left:1px solid #fff}
.compare-row .cell svg{width:18px;height:18px}
.complexity{display:grid;grid-template-columns:209px 136px 136px 136px;height:29px}
.complexity .feature{background:#222;color:#fff;font-family:"Poppins",sans-serif;font-weight:500;font-size:13px;display:flex;align-items:center;padding-left:18px}
.complexity .level{color:#fff;font-family:"Poppins",sans-serif;font-weight:600;font-size:14.5px;display:flex;align-items:center;justify-content:center;border-left:1px solid #fff}
.level.low{background:linear-gradient(120deg,var(--blue) 60%,#5b90d6)}
.level.medium{background:linear-gradient(120deg,var(--green) 60%,#8cca72)}
.level.high{background:linear-gradient(120deg,var(--orange) 60%,#f7b870)}
</style>
</head>
<body>
<svg width="0" height="0" style="position:absolute">
  <defs>
    <symbol id="tick-full" viewBox="0 0 20 20"><circle cx="10" cy="10" r="9.5" fill="#3fae49"/><path d="M5.5 10.3l3 3 6-6.3" fill="none" stroke="#fff" stroke-width="2" stroke-linecap="round" stroke-linejoin="round"/></symbol>
    <symbol id="tick-half" viewBox="0 0 20 20"><path d="M10 .5a9.5 9.5 0 0 0 0 19z" fill="#3fae49"/><path d="M10 .5a9.5 9.5 0 0 1 0 19z" fill="#d9c332"/><path d="M5.5 10.3l3 3 6-6.3" fill="none" stroke="#fff" stroke-width="2" stroke-linecap="round" stroke-linejoin="round"/></symbol>
    <symbol id="tick-most" viewBox="0 0 20 20"><circle cx="10" cy="10" r="9.5" fill="#3fae49"/><path d="M10 10V.5a9.5 9.5 0 0 1 9.5 9.5z" fill="#1d6b3a"/><path d="M5.5 10.3l3 3 6-6.3" fill="none" stroke="#fff" stroke-width="2" stroke-linecap="round" stroke-linejoin="round"/></symbol>
    <symbol id="tick-none" viewBox="0 0 20 20"><circle cx="10" cy="10" r="9.5" fill="#e0262b"/><path d="M5.5 10.3l3 3 6-6.3" fill="none" stroke="#fff" stroke-width="2" stroke-linecap="round" stroke-linejoin="round"/></symbol>
  </defs>
</svg>

<main class="flyer">
  <header class="masthead">
    <svg viewBox="0 0 751 105" width="751" height="105">
      <defs>
        <linearGradient id="mast-blue" x1="0" y1="0" x2="1" y2="1">
          <stop offset="0" stop-color="#2aa4e2"/><stop offset="1" stop-color="#1b4fa8"/>
        </linearGradient>
        <linearGradient id="mast-photo" x1="0" y1="0" x2="1" y2="0">
          <stop offset="0" stop-color="#e8641c"/><stop offset=".45" stop-color="#b9532a"/><stop offset="1" stop-color="#4a3d38"/>
        </linearGradient>
      </defs>
      <rect width="751" height="105" fill="url(#mast-blue)"/>
      <polygon points="15,0 120,0 60,70" fill="#ffffff" opacity=".08"/>
      <polygon points="325,0 382,0 353,40" fill="#9fd6f2"/>
      <polygon points="355,0 371,0 424,105 408,105" fill="#f2701f"/>
      <polygon points="371,0 376,0 430,105 424,105" fill="#ffffff"/>
      <polygon points="376,0 751,0 751,105 430,105" fill="url(#mast-photo)" role="img" aria-label="Photo: installer applying film to an orange car with a heat gun"/>
    </svg>
    <h1 class="masthead-title">PAINT PROTECTION<br>OPTIONS</h1>
  </header>

  <section class="option">
    <div class="option-tab" style="top:130px;height:190px"><span>Ceramic Coatings</span></div>
    <div class="option-copy" style="top:132px">
      <p>Ceramic coatings are liquid polymer coatings that bond to a vehicle’s painted surface. The coatings are formulated to retain the showroom finish by protecting against corrosion and contaminants like UV damage, oxidation, road salt and acid rain.&nbsp; Ceramic coatings give your car a deep, glossy finish that reflects light and makes your paint look more vibrant while greatly extending the paint's lifespan.</p>
      <p>The chemical bonding process improves color depth and leaves a smooth finish. The hydrophobic (water repellent) properties repel water and dirt as well as protect against damaging pollutants.&nbsp; This makes care and maintenance a breeze while retaining the show room finish.&nbsp; Never wax again!</p>
      <ul class="benefits">
        <li>Enhance and retain showroom finish</li>
        <li>Protect against corrosion and contaminants</li>
        <li>Reduce care and maintenance</li>
      </ul>
    </div>
    <svg class="option-photo" style="top:133px" viewBox="0 0 219 178" role="img" aria-label="Photo: gloved hand applying ceramic coating to a blue car panel">
      <defs><linearGradient id="photo-ceramic" x1="0" y1="0" x2="1" y2="1"><stop offset="0" stop-color="#2a49b8"/><stop offset=".6" stop-color="#142d86"/><stop offset="1" stop-color="#3a3f4a"/></linearGradient></defs>
      <rect width="219" height="178" fill="url(#photo-ceramic)"/>
      <polygon points="165,0 175,0 219,55 219,68" fill="#1a4aa0"/>
      <polygon points="175,0 219,0 219,55" fill="#ffffff"/>
    </svg>
  </section>

  <div class="divider"></div>

  <section class="option">
    <div class="option-tab" style="top:345px;height:208px"><span>Paint Protection Film</span></div>
    <div class="option-copy" style="top:362px">
      <p>Paint Protection Film (PPF) is a transparent, thermoplastic urethane film that is applied directly to the car’s painted surfaces. PPF excels at shielding your vehicle from rock chips, scratches, and other physical damage. It has self-healing properties that can repair minor scratches and swirl marks over time.</p>
      <p>Every piece of PPF is custom cut to fit each panel of your vehicle and provide maximum coverage. The film protects your vehicle from scratches, rock chips, staining, corrosion, fading, chemicals, insects, and road debris. It helps keep your paint looking new, saving you money and improving your resale value.</p>
      <ul class="benefits" style="margin-top:7px">
        <li>Protect against rock chips, scratches, and physical damage</li>
        <li>Easily repair minor scratches and swirl marks</li>
        <li>Protect against corrosion and contaminants</li>
      </ul>
    </div>
    <svg class="option-photo" style="top:353px" viewBox="0 0 219 178" role="img" aria-label="Photo: installers stretching wet protection film over a dark car hood">
      <defs><linearGradient id="photo-film" x1="0" y1="0" x2="1" y2="1"><stop offset="0" stop-color="#9fb3ba"/><stop offset=".5" stop-color="#2f4850"/><stop offset="1" stop-color="#b7c6cc"/></linearGradient></defs>
      <rect width="219" height="178" fill="url(#photo-film)"/>
      <polygon points="165,0 175,0 219,55 219,68" fill="#1a4aa0"/>
      <polygon points="175,0 219,0 219,55" fill="#ffffff"/>
    </svg>
  </section>

  <section class="compare">
    <div class="compare-head">
      <div class="head-feature">FEATURE</div>
      <div class="head-option wax"><span class="badge"><i></i></span>Car Wax</div>
      <div class="head-option ceramic"><span class="badge"><i></i></span>Ceramic Coating</div>
      <div class="head-option film"><span class="badge"><i></i></span>Paint Protection Film</div>
    </div>

    <div class="compare-row"><div class="feature"><span class="feature-icon"></span>Duration</div><div class="cell">2 - 4 Weeks</div><div class="cell">3 - 10 Years</div><div class="cell">7 - 10 Years</div></div>
    <div class="compare-row"><div class="feature"><span class="feature-icon"></span>Thickness</div><div class="cell">.5 - 1.5 µm</div><div class="cell">7 - 10 µm</div><div class="cell">200 - 250 µm</div></div>
    <div class="compare-row"><div class="feature"><span class="feature-icon"></span>Gloss Enhancement</div><div class="cell"><svg><use href="#tick-full"/></svg></div><div class="cell"><svg><use href="#tick-full"/></svg></div><div class="cell"><svg><use href="#tick-full"/></svg></div></div>
    <div class="compare-row"><div class="feature"><span class="feature-icon"></span>Acid Rain Damage</div><div class="cell"><svg><use href="#tick-half"/></svg></div><div class="cell"><svg><use href="#tick-full"/></svg></div><div class="cell"><svg><use href="#tick-full"/></svg></div></div>
    <div class="compare-row"><div class="feature"><span class="feature-icon"></span>Corrosion Prevention</div><div class="cell"><svg><use href="#tick-half"/></svg></div><div class="cell"><svg><use href="#tick-full"/></svg></div><div class="cell"><svg><use href="#tick-full"/></svg></div></div>
    <div class="compare-row"><div class="feature"><span class="feature-icon"></span>UV/Oxidation Protection</div><div class="cell"><svg><use href="#tick-half"/></svg></div><div class="cell"><svg><use href="#tick-full"/></svg></div><div class="cell"><svg><use href="#tick-full"/></svg></div></div>
    <div class="compare-row"><div class="feature"><span class="feature-icon"></span>Hard Water Damage</div><div class="cell"><svg><use href="#tick-half"/></svg></div><div class="cell"><svg><use href="#tick-most"/></svg></div><div class="cell"><svg><use href="#tick-full"/></svg></div></div>
    <div class="compare-row"><div class="feature"><span class="feature-icon"></span>Insect Splatter Damage</div><div class="cell"><svg><use href="#tick-half"/></svg></div><div class="cell"><svg><use href="#tick-most"/></svg></div><div class="cell"><svg><use href="#tick-full"/></svg></div></div>
    <div class="compare-row"><div class="feature"><span class="feature-icon"></span>Chip Protection</div><div class="cell"><svg><use href="#tick-none"/></svg></div><div class="cell"><svg><use href="#tick-half"/></svg></div><div class="cell"><svg><use href="#tick-full"/></svg></div></div>
    <div class="compare-row"><div class="feature"><span class="feature-icon"></span>Scratch Protection</div><div class="cell"><svg><use href="#tick-none"/></svg></div><div class="cell"><svg><use href="#tick-half"/></svg></div><div class="cell"><svg><use href="#tick-full"/></svg></div></div>
    <div class="compare-row"><div class="feature"><span class="feature-icon"></span>Swirl Protection</div><div class="cell"><svg><use href="#tick-none"/></svg></div><div class="cell"><svg><use href="#tick-none"/></svg></div><div class="cell"><svg><use href="#tick-full"/></svg></div></div>

    <div class="complexity">
      <div class="feature">Application Complexity</div>
      <div class="level low">Low</div>
      <div class="level medium">Medium</div>
      <div class="level high">High</div>
    </div>
  </section>
</main>
</body>
</html>
```